Combat Sports news website design

Redesigning our existing website to make it more modern, responsive and suitable for our needs. The design needs to take in to account all aspects of our current website structure and services. View the existing website at https://www.brawlpulse.co.nz

Particular attention should be paid to our livestream service, which is growing and needs to be much more user friendly to the current experience.

The homepage, article listings and article pages need designs.

Target Market(s)

Combat sports fans

Industry/Entity Type

Media

Coding

Number of Pages Required

5+ page

Font styles to use
Sans Serif

Requirements
Must have
• All the functionality of the existing website must be taken in to account, and improved upon.
New design must incorporate our existing logo/colour scheme as this has only just been designed.

```html
<!DOCTYPE html>
<html lang="en">
<head>
<meta charset="utf-8">
<title>Brawl Pulse — Home</title>
<link href="https://fonts.googleapis.com/css2?family=Bebas+Neue&family=Open+Sans:wght@400&display=swap" rel="stylesheet">
<style>
:root{
  --ink:#161616;
  --red:#b0222b;
  --footer:#a6202a;
  --muted:#7a7a7a;
  --body:#3a3a3a;
  --line:#cfcfcf;
  --bg:#ffffff;
}
*{box-sizing:border-box;margin:0;padding:0}
html,body{width:859px;height:1200px;overflow:hidden;background:var(--bg)}
body{position:relative;font-family:"Open Sans",sans-serif;color:var(--ink)}
.display{font-family:"Bebas Neue",sans-serif;font-weight:400;color:var(--ink)}
.abs{position:absolute}
a{color:inherit;text-decoration:none}
.read-more{color:var(--red)}

.topbar{left:0;top:0;width:859px;height:69px;border-bottom:1px solid #9a9a9a}
.social{left:39px;top:28px;display:flex;gap:13px}
.social span{width:16px;height:16px;border-radius:50%;background:var(--ink);display:block}
.brand{left:0;width:859px;top:13px;text-align:center;font-family:"Bebas Neue",sans-serif;font-size:24px;line-height:21px;color:var(--red);letter-spacing:1px}
.account{right:52px;top:26px;display:flex;gap:28px;font-size:15px}

.mainnav{left:0;top:69px;width:859px;height:52px;border-bottom:1px solid #9a9a9a}
.mainnav a{position:absolute;top:15px;font-family:"Bebas Neue",sans-serif;font-size:20px;line-height:22px;color:var(--ink)}
.mainnav a.active{color:var(--red)}
.search{position:absolute;left:801px;top:16px}

.ph{display:block}
.hero-img{left:40px;top:154px;width:384px;height:229px;background:linear-gradient(135deg,#8d8a8a,#3d3a3a 55%,#5a2a2c)}
.hero-meta{left:437px;top:199px;font-size:14px;color:var(--muted)}
.hero-title{left:437px;top:223px;width:380px;font-size:30px;line-height:35px}
.hero-text{left:439px;top:300px;width:350px;font-size:13px;line-height:18.5px;color:var(--body)}

.section-title{font-size:28px;line-height:28px}
.see-more{right:39px;top:428px;font-family:"Bebas Neue",sans-serif;font-size:20px;color:var(--red)}

.card{top:475px;width:186px}
.card .ph{width:186px;height:111px}
.card h3{margin-top:10px;font-size:16.5px;line-height:20px}
.card p{font-size:11.5px;color:var(--muted);margin-top:1px}

.story{left:39px;width:470px;height:94px}
.story .ph{position:absolute;left:0;top:0;width:157px;height:94px}
.story h3{position:absolute;left:175px;top:4px;font-size:20px;line-height:22px;white-space:nowrap}
.story .meta{position:absolute;left:175px;top:30px;font-size:11.5px;color:var(--muted)}
.story .excerpt{position:absolute;left:175px;top:57px;width:290px;font-size:12px;line-height:16px;color:var(--body)}

.editor{left:567px;top:744px;width:252px;height:356px;border:1px solid #b8b8b8}
.editor h2{position:absolute;left:14px;top:17px;font-size:19px;line-height:20px}
.editor .rule{position:absolute;left:14px;top:41px;width:223px;height:1px;background:var(--line)}
.pick{position:absolute;left:14px;width:224px;height:61px}
.pick .ph{position:absolute;left:0;top:0;width:70px;height:61px}
.pick .meta{position:absolute;left:78px;top:9px;font-size:8.5px;color:var(--muted)}
.pick h4{position:absolute;left:78px;top:20px;width:150px;font-family:"Bebas Neue",sans-serif;font-weight:400;font-size:14.5px;line-height:17.5px}

.footer{left:0;top:1168px;width:859px;height:32px;background:var(--footer);color:#fff}
.footer .copy{position:absolute;left:39px;top:7px;font-family:"Bebas Neue",sans-serif;font-size:14px}
.footer nav{position:absolute;right:39px;top:9px;display:flex;gap:21px;font-size:8.5px}
</style>
</head>
<body>

<header class="abs topbar">
  <div class="abs social" aria-label="Social links"><span></span><span></span><span></span></div>
  <div class="abs brand">Brawl<br>Pulse</div>
  <nav class="abs account display"><a href="#">Contact</a><a href="#">Login</a></nav>
</header>

<nav class="abs mainnav">
  <a href="#" style="left:40px">Home</a>
  <a href="#" class="active" style="left:126px">MMA</a>
  <a href="#" style="left:207px">Kickboxing</a>
  <a href="#" style="left:329px">Boxing</a>
  <a href="#" style="left:424px">Wrestling</a>
  <a href="#" style="left:542px">GFC</a>
  <a href="#" style="left:616px">APEXFC</a>
  <a href="#" style="left:706px">Live Event</a>
  <svg class="search" width="18" height="18" viewBox="0 0 18 18" fill="none" stroke="#161616" stroke-width="1.6"><circle cx="8" cy="8" r="6.5"/><line x1="12.8" y1="12.8" x2="17" y2="17"/></svg>
</nav>

<section>
  <div class="abs ph hero-img" role="img" aria-label="Fighter speaking to press at a media day"></div>
  <p class="abs hero-meta">Popular News • 14 April 2021</p>
  <h1 class="abs hero-title display">Rise to Fight 9 Results: Tama Reid Wins RTF9 Debut</h1>
  <p class="abs hero-text">The 20-year-old has been training for 11 years. She started Taekwondo when she was nine-years-old in her hometown of Opotiki. <a href="#" class="read-more" style="font-size:14px">Read more</a></p>
</section>

<h2 class="abs section-title display" style="left:40px;top:425px">You Might Like</h2>
<a href="#" class="abs see-more">See More</a>

<article class="abs card" style="left:40px">
  <div class="ph" role="img" aria-label="Fight night event poster with lineup of fighters" style="background:linear-gradient(180deg,#c8282c,#5a4a48 40%,#3a3436)"></div>
  <h3 class="display">Kane Ellis Aims to Stay Busy in 2021</h3>
  <p>News • 14 April 2021</p>
</article>
<article class="abs card" style="left:238.5px">
  <div class="ph" role="img" aria-label="Black and white event poster with fighter lineup" style="background:linear-gradient(180deg,#1e1e1e,#6a6a6a 70%,#2a2a2a)"></div>
  <h3 class="display">Rise to Fight 9 Results: Tama Reid Wins RTF9 Debut</h3>
  <p>News • 14 April 2021</p>
</article>
<article class="abs card" style="left:436.5px">
  <div class="ph" role="img" aria-label="Event poster with two headline fighters" style="background:linear-gradient(135deg,#2a2a2a,#6a5246 50%,#3a3a3a)"></div>
  <h3 class="display">Kane Ellis Aims to Stay Busy in 2021</h3>
  <p>News • 14 April 2021</p>
</article>
<article class="abs card" style="left:634px">
  <div class="ph" role="img" aria-label="Blue event poster with fight card matchups" style="background:linear-gradient(180deg,#1f4f9a,#4a6aa8 50%,#2a3d70)"></div>
  <h3 class="display">Plans for Ben Rowe to Fight at GFC</h3>
  <p style="margin-top:-4px">News • 14 April 2021</p>
</article>

<h2 class="abs section-title display" style="left:40px;top:694px">Recent News</h2>

<article class="abs story" style="top:744px">
  <div class="ph" role="img" aria-label="Black and white photo of a fighter in the ring" style="background:linear-gradient(135deg,#111,#777 50%,#222)"></div>
  <h3 class="display">Kane Ellis Aims to Stay Busy in 2021</h3>
  <p class="meta">News • 14 April 2021</p>
  <p class="excerpt">Logan 'Iron' Hale is a veteran of the New Zealand fight game, boasting 53.. <a href="#" class="read-more">Read more</a></p>
</article>
<article class="abs story" style="top:879px">
  <div class="ph" role="img" aria-label="Champion posing with title belt in the ring" style="background:linear-gradient(135deg,#1a1f3a,#8a5a44 50%,#1a1a2a)"></div>
  <h3 class="display">Sheldon Two-Time South Island...</h3>
  <p class="meta">News • 13 April 2021</p>
  <p class="excerpt">Noah Sheldon (Strike Lab Queenstown) won the WKSA South Island.. <a href="#" class="read-more">Read more</a></p>
</article>
<article class="abs story" style="top:1014px">
  <div class="ph" role="img" aria-label="Fighter speaking to press at a media day" style="background:linear-gradient(135deg,#8d8a8a,#3d3a3a 55%,#5a2a2c)"></div>
  <h3 class="display">Plans for Ben Rowe to Fight at GFC</h3>
  <p class="meta">News • 12 April 2021</p>
  <p class="excerpt">Noah Sheldon (Strike Lab Queenstown) won the WKSA South Island.. <a href="#" class="read-more">Read more</a></p>
</article>

<aside class="abs editor">
  <h2 class="display">Editor Choice's</h2>
  <div class="rule"></div>
  <div class="pick" style="top:56px">
    <div class="ph" role="img" aria-label="Referee raising winner's hand in the ring" style="background:linear-gradient(135deg,#3a3a3a,#9a9a9a 50%,#444)"></div>
    <p class="meta">News • 14 April 2021</p>
    <h4>Rise to Fight 9 Results: Tama Reid Wins RTF9 Debut</h4>
  </div>
  <div class="pick" style="top:132px">
    <div class="ph" role="img" aria-label="Champion posing with title belt" style="background:linear-gradient(135deg,#1a1f3a,#8a5a44 50%,#1a1a2a)"></div>
    <p class="meta">News • 14 April 2021</p>
    <h4>Sheldon Two-Time South Island...</h4>
  </div>
  <div class="pick" style="top:207px">
    <div class="ph" role="img" aria-label="Fighter at a media day" style="background:linear-gradient(135deg,#8d8a8a,#3d3a3a 55%,#5a2a2c)"></div>
    <p class="meta">News • 14 April 2021</p>
    <h4>Plans for Ben Rowe to Fight at GFC</h4>
  </div>
  <div class="pick" style="top:281px">
    <div class="ph" role="img" aria-label="Black and white fighter portrait" style="background:linear-gradient(135deg,#111,#777 50%,#222)"></div>
    <p class="meta">News • 14 April 2021</p>
    <h4>Kane Ellis Aims to Stay Busy in 2021</h4>
  </div>
</aside>

<footer class="abs footer">
  <p class="copy">Copyright ©2021 Brawl Media Ltd.</p>
  <nav><a href="#">Site Terms</a><a href="#">Privacy</a><a href="#">Advertisement</a><a href="#">Contact Us</a></nav>
</footer>

</body>
</html>
```